Product label and brand logo for Superfood powder

We need a product label (incl. logo) for a new plant-based Superfood powder called "MyLunaBrisa Health & Wellness Protein" ("MyLunaBrisa" being the brand). The powder formula is comprised of various Superfoods that each offer a unique benefit to the customer. On top of that the formular includes real coffee for excellent taste. This is a premium product and some ingredients even come from organic sources. I've included an extended briefing with examples as a PDF. The final design should communicate wellbeing, health, wellness rather than target the sport and fitness crowd (as most protein powders do).
Target Market(s)
Health & Wellness Space
Industry/Entity Type
Health And Wellness
Requirements
Must have
- Please see attached PDF.
Nice to have

```html
<!DOCTYPE html>
<html lang="de">
<head>
<meta charset="utf-8">
<title>MyLunaBrisa Health &amp; Wellness Protein – Etikett</title>
<link rel="stylesheet" href="https://fonts.googleapis.com/css2?family=Raleway:wght@300;400;500;600;700;800&display=swap">
<style>
  :root{
    --stage:#6b6b6b;
    --label-white:#ffffff;
    --leaf-tint:#eceee9;
    --brand-green:#55803a;
    --brand-green-dark:#44692d;
    --coffee:#4a2c1d;
    --coffee-light:#7a4a2e;
    --white:#ffffff;
  }
  *{box-sizing:border-box;margin:0;padding:0}
  html,body{width:1200px;height:1200px;overflow:hidden}
  body{background:var(--stage);font-family:'Raleway',sans-serif;position:relative}

  .label{position:absolute;top:442px;height:530px;border-radius:14px;overflow:hidden;background:var(--brand-green);color:var(--white)}
  .label--front{left:130px;width:424px}
  .label--back{left:658px;width:432px}
  .label > *{position:absolute}

  .label__top{left:0;top:0;width:100%;height:190px;
    background:linear-gradient(135deg,var(--label-white) 0%,var(--leaf-tint) 50%,var(--label-white) 100%)}
  .label--back .label__top{height:188px}

  .brand-name{left:0;right:0;text-align:center;font-weight:400;color:var(--brand-green);line-height:1;letter-spacing:.5px}
  .label--front .brand-name{top:78px;font-size:38px}
  .label--back .brand-name{top:62px;font-size:30px}

  .badge-vegan{left:324px;top:38px;width:48px;height:48px;border-radius:50%;border:3px solid var(--brand-green);background:var(--white)}

  .subtitle{left:0;right:0;text-align:center;font-weight:400;line-height:1}
  .title{left:0;right:0;text-align:center;font-weight:700;letter-spacing:1px;line-height:1}
  .label--front .subtitle{top:214px;font-size:26px}
  .label--front .title{top:242px;font-size:48px}

  .flavour{left:84px;width:254px;top:295px;height:24px;border-radius:12px;background:var(--coffee);
    font-weight:700;font-size:17px;line-height:24px;text-align:center}
  .beans{left:178px;top:326px;width:68px;height:50px;border-radius:40%;
    background:radial-gradient(circle at 40% 40%,var(--coffee-light),var(--coffee) 70%)}
  .claim{left:0;right:0;top:381px;text-align:center;font-size:15px;font-weight:500;line-height:1}

  .stats{left:104px;width:216px;top:404px;display:flex;justify-content:space-between}
  .stat{flex:1;border-left:1px solid rgba(255,255,255,.75);text-align:center}
  .stat:first-child{border-left:none}
  .stat__value{font-size:19px;font-weight:700;line-height:22px}
  .stat__unit{font-size:5.5px;font-weight:600;letter-spacing:.4px;text-transform:uppercase;line-height:1.2}

  .icon{top:456px;width:50px;text-align:center;font-size:5.5px;line-height:1.2}
  .icon--gluten{left:119px}
  .icon--lactose{left:187px}
  .icon--sugar{left:251px}
  .icon__circle{width:30px;height:30px;border-radius:50%;border:1.5px solid var(--coffee);margin:0 auto 3px;background:rgba(0,0,0,.06)}

  .net{left:0;right:0;top:502px;text-align:center;font-size:14px;font-weight:500;line-height:1}
  .net b{font-weight:700}

  .label--back .subtitle{top:143px;font-size:16px;color:var(--brand-green-dark)}
  .label--back .title{top:159px;font-size:28px;color:var(--brand-green-dark)}
  .back__rule{left:70px;right:0;top:193px;height:2px;background:var(--coffee)}
  .back__flavour{left:150px;width:158px;top:192px;height:14px;border-radius:7px;background:var(--coffee);
    font-size:8.5px;font-weight:700;text-align:center;line-height:14px}

  .nutrition{left:74px;top:212px;width:294px;border-collapse:collapse;font-size:7.5px;line-height:1}
  .nutrition th,.nutrition td{border:1px solid rgba(255,255,255,.8);padding:2px 4px;text-align:left;font-weight:500;height:12px}
  .nutrition th{font-weight:700}
  .nutrition td:first-child{width:150px}
  .nutrition .indent{padding-left:10px}

  .info{left:74px;width:294px;top:356px;font-size:7.5px;line-height:1.4}
  .info b{font-weight:700}

  .code-box{left:74px;top:425px;width:124px;height:56px;background:var(--white)}
  .made-in{left:74px;top:484px;width:126px;font-size:6.5px;border-top:1px solid rgba(255,255,255,.8);padding-top:2px;line-height:1}
  .distributor{left:204px;top:425px;width:164px;font-size:6.5px;line-height:1.35;border-left:1px solid rgba(255,255,255,.8);padding-left:5px}
</style>
</head>
<body>

<section class="label label--front">
  <div class="label__top" role="img" aria-label="Zarte helle Blattranken als Hintergrund"></div>
  <p class="brand-name">MyLunaBrisa</p>
  <div class="badge-vegan" role="img" aria-label="Vegan-Siegel"></div>
  <p class="subtitle">Health &amp; Wellness</p>
  <h1 class="title">PROTEIN</h1>
  <p class="flavour">Kaffeegeschmack</p>
  <div class="beans" role="img" aria-label="Geröstete Kaffeebohnen"></div>
  <p class="claim">Mit echtem Kaffee</p>
  <div class="stats">
    <div class="stat"><div class="stat__value">20g</div><div class="stat__unit">Protein</div></div>
    <div class="stat"><div class="stat__value">4g</div><div class="stat__unit">BCAA</div></div>
    <div class="stat"><div class="stat__value">4g</div><div class="stat__unit">Glutamin</div></div>
    <div class="stat"><div class="stat__value">+</div><div class="stat__unit">Vitamine<br>Mineralstoffe</div></div>
  </div>
  <div class="icon icon--gluten"><div class="icon__circle"></div>Glutenfrei</div>
  <div class="icon icon--lactose"><div class="icon__circle"></div>Laktosefrei</div>
  <div class="icon icon--sugar"><div class="icon__circle"></div>Zuckerfrei</div>
  <p class="net">℮ 1.000 g / <b>25</b> Portionen</p>
</section>

<section class="label label--back">
  <div class="label__top" role="img" aria-label="Zarte helle Blattranken als Hintergrund"></div>
  <p class="brand-name">MyLunaBrisa</p>
  <p class="subtitle">Health &amp; Wellness</p>
  <h2 class="title">PROTEIN</h2>
  <div class="back__rule"></div>
  <p class="back__flavour">Kaffeegeschmack</p>

  <table class="nutrition">
    <tr><th>Nährwerte</th><th>pro 100 g</th><th>pro 30 g</th></tr>
    <tr><th>Brennwert</th><td>1597 kJ</td><td>479 kJ</td></tr>
    <tr><th>Brennwert</th><td>378 kcal</td><td>113 kcal</td></tr>
    <tr><th>Fett</th><td>5.5 g</td><td>1.6 g</td></tr>
    <tr><td class="indent">davon gesättigte Fettsäuren</td><td>1.8 g</td><td>0.56 g</td></tr>
    <tr><th>Kohlenhydrate</th><td>3 g</td><td>0.92 g</td></tr>
    <tr><td class="indent">davon Zucker</td><td>0 g</td><td>0 g</td></tr>
    <tr><th>Ballaststoffe</th><td>7.2 g</td><td>2.1 g</td></tr>
    <tr><th>Eiweiß</th><td>75.2 g</td><td>22.5 g</td></tr>
    <tr><th>Salz*</th><td>0.91 g</td><td>0.27 g</td></tr>
  </table>

  <div class="info">
    <p><b>Zutaten:</b> Erbsenprotein, Reisprotein, Kaffee, Kakao, Kürbiskern, Hanf, Leinsamen, Aroma.</p>
    <p><b>Verzehrempfehlung:</b> 40 g Pulver im Shaker mit 400-500 ml Wasser mischen und gut schütteln.</p>
    <p>Mindestens haltbar bis Ende und Chargennummer siehe Boden.</p>
  </div>

  <div class="code-box"></div>
  <p class="made-in">Hergestellt in Deutschland</p>
  <div class="distributor">
    Vertrieb/Distributor: MyLunaBrisa OG,<br>
    Lindenweg 12, 8010 Talstadt,<br>
    Österreich<br>
    Telefon: +43 720 000111222<br>
    www.mylunabrisa.example<br>
    social: mylunabrisa
  </div>

  <p class="net">℮ 1.000 g / <b>25</b> Portionen</p>
</section>

</body>
</html>
```